Industrial CNC laser cutting machine manufacturer needs a website designed

We need a website design for our company that re manufactures CNC laser cutting machines, we take old retired machines and completely re manufacture them from the ground up bringing them into the latest technology with all new parts and give them a new lease on life for a fraction of the cost of a new machine.

Machines can be fully customized to suit customers requirements too

My logo will need to be integrated and I want the website to look clean and modern

I will probably want 4 pages,Home, pictures, machines for sale and contact

```html
<!DOCTYPE html>
<html lang="en">
<head>
<meta charset="utf-8">
<title>Machines For Sale – Rexcut Machine Works</title>
<link href="https://fonts.googleapis.com/css2?family=Bebas+Neue&family=Poppins:wght@400;500;600&display=swap" rel="stylesheet">
<style>
:root{
  --red:#e03232;
  --ink:#1f2026;
  --dark:#1e1f27;
  --darker:#17181e;
  --grey-bg:#e8e8e9;
  --text:#555;
  --line:#d9d9d9;
  --white:#fff;
}
*{margin:0;padding:0;box-sizing:border-box}
html,body{width:1200px;height:3266px;overflow:hidden}
body{position:relative;background:var(--white);font-family:"Poppins",sans-serif;color:var(--ink)}
.display{font-family:"Bebas Neue",sans-serif;letter-spacing:.2px}
a{color:inherit;text-decoration:none}

/* hero */
.hero{position:absolute;left:0;top:0;width:1200px;height:550px;background:var(--grey-bg);overflow:hidden}
.hero svg.bg{position:absolute;inset:0}
.hero-title{position:absolute;left:86px;top:272px;font-size:64px;line-height:1;color:var(--ink)}
.crumbs{position:absolute;left:88px;top:347px;display:flex;align-items:center;gap:10px;font-family:"Bebas Neue",sans-serif;font-size:21px}
.crumbs .here{color:var(--red)}
.hero-media{position:absolute;left:551px;top:165px;width:602px;height:310px;border-radius:4px;background:linear-gradient(120deg,#d8d8da 0%,#e4393a 45%,#c9c9cb 100%);opacity:.9}

/* header */
.header{position:absolute;left:89px;top:27px;width:1022px;height:88px;background:var(--white);box-shadow:0 6px 18px rgba(0,0,0,.08);display:flex;align-items:center}
.brand{position:absolute;left:35px;top:30px;display:flex;align-items:center;gap:10px}
.brand-mark{width:26px;height:26px;background:var(--red)}
.brand-name{font-family:"Bebas Neue",sans-serif;font-size:30px;color:#6b6b6b;line-height:1}
.nav{position:absolute;left:385px;top:0;height:88px;display:flex;align-items:center;gap:22px;font-family:"Bebas Neue",sans-serif;font-size:18px}
.nav a{position:relative;height:88px;display:flex;align-items:center}
.nav a.active{color:var(--red)}
.nav a.active::before{content:"";position:absolute;left:0;right:0;top:0;height:2px;background:var(--red)}
.lang{position:absolute;left:755px;top:34px;display:flex;align-items:center;gap:8px;font-size:11px;font-weight:500}
.flag{width:18px;height:18px;border-radius:50%;background:linear-gradient(#d94a4a 50%,#3b4ea0 50%)}
.h-sep{position:absolute;left:856px;top:0;width:1px;height:88px;background:#eee}
.tools{position:absolute;left:893px;top:32px;display:flex;gap:12px}
.cart{position:relative}
.cart b{position:absolute;right:-6px;top:-4px;width:13px;height:13px;border-radius:50%;background:var(--red);color:#fff;font-size:8px;display:flex;align-items:center;justify-content:center}

/* products */
.section-title{position:absolute;left:0;width:1200px;top:634px;text-align:center;font-size:29px}
.product{position:absolute;left:185px;width:830px;height:251px}
.product .media{position:absolute;top:0;width:323px;height:251px;background:linear-gradient(135deg,#f2f2f3 0%,#e6e6e8 55%,#f0f0f1 100%)}
.product .info{position:absolute;top:0;width:490px}
.product.img-left .media{left:0}
.product.img-left .info{left:362px}
.product.img-right .media{left:507px}
.product.img-right .info{left:3px}
.badge{position:absolute;top:14px;left:2px;background:var(--red);color:#fff;font-size:11px;font-weight:600;padding:2px 6px;line-height:17px}
.product h3{position:absolute;top:45px;left:2px;font-family:"Bebas Neue",sans-serif;font-weight:400;font-size:28px;white-space:nowrap;line-height:1}
.specs{position:absolute;top:86px;left:2px;list-style:none;font-size:13.5px;line-height:25px;color:var(--text)}
.actions{position:absolute;top:206px;left:0;display:flex;gap:9px}
.btn{height:33px;border:1px solid var(--line);display:flex;align-items:center;justify-content:center;font-size:11.5px;font-weight:500;color:#666;letter-spacing:.3px}
.btn:nth-child(1){width:118px}.btn:nth-child(2){width:120px}.btn:nth-child(3){width:119px}

/* pagination */
.pager{position:absolute;left:361px;top:2393px;display:flex;align-items:center;height:42px}
.pg-btn{width:115px;height:42px;display:flex;align-items:center;justify-content:center;gap:8px;font-size:13px;font-weight:500}
.pg-prev{background:#ececec;color:#777}
.pg-next{background:#707070;color:#fff;margin-left:27px}
.pg-num{font-size:17px;font-weight:500;width:52px;text-align:center}
.pg-num.current{width:46px;height:46px;border-radius:50%;background:var(--red);color:#fff;display:flex;align-items:center;justify-content:center;margin:0 4px}

/* footer */
.footer-bg{position:absolute;left:0;top:2440px}
.newsletter-title{position:absolute;left:0;width:1200px;top:2700px;text-align:center;color:#fff;font-size:46px;line-height:1}
.subscribe{position:absolute;left:340px;top:2760px;display:flex;height:46px}
.subscribe .field{width:401px;background:#fff;display:flex;align-items:center;gap:10px;padding-left:22px;font-size:13.5px;color:#666}
.subscribe .go{width:119px;background:var(--red);color:#fff;font-weight:600;font-size:13.5px;display:flex;align-items:center;justify-content:center}
.col{position:absolute;top:2866px;color:#fff}
.col h4{font-family:"Bebas Neue",sans-serif;font-weight:400;font-size:25px;margin-bottom:18px}
.col ul{list-style:none;font-size:13px;line-height:28.5px}
.col li::before{content:"› ";color:#ccc}
.contact li::before{content:none}
.contact li{display:flex;gap:10px;line-height:21px;margin-bottom:14px;font-size:14px}
.contact svg{flex:none;margin-top:4px}
.bottom-bar{position:absolute;left:0;top:3164px;width:1200px;height:102px;background:var(--darker)}
.bottom-bar .brand{left:155px;top:36px}
.bottom-bar .brand-name{color:#8a8a8e}
.copy{position:absolute;left:0;width:1200px;top:43px;text-align:center;color:#fff;font-size:12px;font-weight:500}
.social{position:absolute;left:919px;top:34px;display:flex;gap:13px}
.social span{width:33px;height:33px;border-radius:50%;background:#2c2d35}
</style>
</head>
<body>

<section class="hero">
  <svg class="bg" width="1200" height="550" aria-hidden="true">
    <polygon points="0,550 1200,160 1200,550" fill="#f4f4f5"/>
  </svg>
  <h1 class="hero-title display">Machines For Sale</h1>
  <div class="crumbs">
    <svg width="22" height="18" viewBox="0 0 22 18"><path d="M11 0 L22 9 H19 V18 H13 V12 H9 V18 H3 V9 H0 Z" fill="#222"/></svg>
    <span>Home</span><span>|</span><span class="here">Machines For Sale</span>
  </div>
  <div class="hero-media" role="img" aria-label="Red and white fiber laser cutting machine with control cabinet"></div>
</section>

<header class="header">
  <a class="brand" href="#"><span class="brand-mark"></span><span class="brand-name">Rexcut Machine Works</span></a>
  <nav class="nav">
    <a href="#">Home</a><a href="#">Gallery</a><a class="active" href="#">Machines For Sale</a><a href="#">Contact Us</a>
  </nav>
  <div class="lang"><span class="flag"></span>ENG
    <svg width="8" height="6" viewBox="0 0 8 6"><path d="M1 1 L4 4 L7 1" stroke="#333" stroke-width="1.4" fill="none"/></svg></div>
  <span class="h-sep"></span>
  <div class="tools">
    <svg width="20" height="22" viewBox="0 0 20 22" fill="none" stroke="#333" stroke-width="1.6"><circle cx="10" cy="7" r="5"/><path d="M2 21 C2 15 18 15 18 21"/></svg>
    <svg width="20" height="22" viewBox="0 0 20 22" fill="none" stroke="#333" stroke-width="1.6"><circle cx="8.5" cy="9" r="6.5"/><path d="M13 14 L19 20"/></svg>
    <span class="cart"><svg width="22" height="22" viewBox="0 0 22 22" fill="none" stroke="#333" stroke-width="1.6"><path d="M1 3 H4 L7 15 H18 L20 6 H5"/><circle cx="8" cy="19" r="1.5"/><circle cx="17" cy="19" r="1.5"/></svg><b>0</b></span>
  </div>
</header>

<h2 class="section-title display">Pipe &amp; Sheet Metal Cutting Machine</h2>

<article class="product img-left" style="top:709px">
  <div class="media" role="img" aria-label="Enclosed single platform laser cutting machine"></div>
  <div class="info">
    <span class="badge">F8025TDE</span>
    <h3>E Series Single Platform Laser Cutting Machine</h3>
    <ol class="specs"><li>1. Laser Power: 1000W-15000W</li><li>2. Cutting Thickness: 0.5-60mm</li><li>3. Dual automatic exchange table to save loading and unloading time</li><li>4. Enclosed design to protect from dust</li></ol>
    <div class="actions"><a class="btn">FREE SAMPLE</a><a class="btn">SEND INQUIRY</a><a class="btn">MORE DETAILS</a></div>
  </div>
</article>

<article class="product img-right" style="top:1049px">
  <div class="info">
    <span class="badge">F8025TDE</span>
    <h3>HDE Series Enclosed Exchanged Dual</h3>
    <ol class="specs"><li>1. Laser Power: 1000W-15000W</li><li>2. Cutting Thickness: 0.5-60mm</li><li>3. Dual automatic exchange table to save loading and unloading time</li><li>4. Enclosed design to protect from dust</li></ol>
    <div class="actions"><a class="btn">FREE SAMPLE</a><a class="btn">SEND INQUIRY</a><a class="btn">MORE DETAILS</a></div>
  </div>
  <div class="media" role="img" aria-label="Enclosed dual exchange table laser cutter"></div>
</article>

<article class="product img-left" style="top:1387px">
  <div class="media" role="img" aria-label="High power enclosed laser cutting machine"></div>
  <div class="info">
    <span class="badge">F8025TDE</span>
    <h3>TDE Series High Power Laser Cutting Machine</h3>
    <ol class="specs"><li>1. Laser Power: 1000W-15000W</li><li>2. Cutting Thickness: 0.5-60mm</li><li>3. Dual automatic exchange table to save loading and unloading time</li><li>4. Enclosed design to protect from dust</li></ol>
    <div class="actions"><a class="btn">FREE SAMPLE</a><a class="btn">SEND INQUIRY</a><a class="btn">MORE DETAILS</a></div>
  </div>
</article>

<article class="product img-right" style="top:1727px">
  <div class="info">
    <span class="badge">F8025TDE</span>
    <h3>HDE Series Enclosed Exchanged Dual</h3>
    <ol class="specs"><li>1. Laser Power: 1000W-15000W</li><li>2. Cutting Thickness: 0.5-60mm</li><li>3. Dual automatic exchange table to save loading and unloading time</li><li>4. Enclosed design to protect from dust</li></ol>
    <div class="actions"><a class="btn">FREE SAMPLE</a><a class="btn">SEND INQUIRY</a><a class="btn">MORE DETAILS</a></div>
  </div>
  <div class="media" role="img" aria-label="Open flatbed laser cutting table"></div>
</article>

<article class="product img-left" style="top:2067px">
  <div class="media" role="img" aria-label="Pipe and sheet laser cutting machine in white and teal"></div>
  <div class="info">
    <span class="badge">F8025TDE</span>
    <h3>TDE Series High Power Laser Cutting Machine</h3>
    <ol class="specs"><li>1. Laser Power: 1000W-15000W</li><li>2. Cutting Thickness: 0.5-60mm</li><li>3. Dual automatic exchange table to save loading and unloading time</li><li>4. Enclosed design to protect from dust</li></ol>
    <div class="actions"><a class="btn">FREE SAMPLE</a><a class="btn">SEND INQUIRY</a><a class="btn">MORE DETAILS</a></div>
  </div>
</article>

<nav class="pager">
  <a class="pg-btn pg-prev"><svg width="8" height="12" viewBox="0 0 8 12"><path d="M6 1 L1 6 L6 11" stroke="#777" stroke-width="1.8" fill="none"/></svg>PREV</a>
  <span class="pg-num" style="margin-left:4px">1</span>
  <span class="pg-num current">2</span>
  <span class="pg-num">3</span>
  <span class="pg-num" style="width:24px">...</span>
  <span class="pg-num">82</span>
  <a class="pg-btn pg-next">NEXT<svg width="8" height="12" viewBox="0 0 8 12"><path d="M2 1 L7 6 L2 11" stroke="#fff" stroke-width="1.8" fill="none"/></svg></a>
</nav>

<svg class="footer-bg" width="1200" height="826" aria-hidden="true">
  <polygon points="0,272 1200,12 1200,826 0,826" fill="var(--dark)"/>
  <polygon points="0,272 1200,12 0,317" fill="var(--red)"/>
</svg>

<h2 class="newsletter-title display">Newsletter</h2>
<form class="subscribe">
  <label class="field"><svg width="14" height="11" viewBox="0 0 14 11"><rect width="14" height="11" fill="#aaa"/><path d="M0 0 L7 6 L14 0" stroke="#fff" fill="none"/></svg>Enter your email address</label>
  <span class="go">SUBSCRIBE</span>
</form>

<div class="col" style="left:155px"><h4>Product</h4>
  <ul><li>Fiber Laser Cutting</li><li>CO2 Laser Cutting</li><li>Laser Machine Welding</li><li>Laser Marking</li><li>Laser Machine Cleaning</li></ul></div>
<div class="col" style="left:409px"><h4>Company</h4>
  <ul><li>VR Overall View</li><li>Company Profile</li><li>Certificate</li><li>Contact</li><li>Customer</li></ul></div>
<div class="col" style="left:611px"><h4>Supply Chain</h4>
  <ul><li>General Information</li><li>Existing Suppliers</li><li>Become A Supplier</li><li>Customer Service</li></ul></div>
<div class="col contact" style="left:848px"><h4>Contact Info</h4>
  <ul>
    <li><svg width="13" height="10" viewBox="0 0 13 10"><rect width="13" height="10" fill="var(--red)"/><path d="M0 0 L6.5 5 L13 0" stroke="#1e1f27" fill="none"/></svg><span>Email:<br>www.example.com</span></li>
    <li><svg width="13" height="13" viewBox="0 0 13 13"><path d="M2 1 L5 1 L6 4 L4 5 C5 7 6 8 8 9 L9 7 L12 8 L12 11 C6 12 1 7 2 1Z" fill="var(--red)"/></svg><span>Phone:<br>1 (+08) 123-456-78</span></li>
    <li><svg width="11" height="15" viewBox="0 0 11 15"><path d="M5.5 0 C2.5 0 0 2.4 0 5.4 C0 9 5.5 15 5.5 15 C5.5 15 11 9 11 5.4 C11 2.4 8.5 0 5.5 0Z" fill="var(--red)"/><circle cx="5.5" cy="5.5" r="2" fill="#1e1f27"/></svg><span>Location:<br>Some address line goes<br>here city name</span></li>
  </ul></div>

<footer class="bottom-bar">
  <a class="brand" href="#"><span class="brand-mark"></span><span class="brand-name">Rexcut Machine Works</span></a>
  <p class="copy">© 2020. ALL RIGHTS RESERVED</p>
  <div class="social"><span></span><span></span><span></span></div>
</footer>

</body>
</html>
```